Professional BIO Template with photo and logo

Hello,
I need a professional Bio template developed via Microsoft WORD ASAP!!!!! I would like to just be able to add the text I need to add. So resize-able text boxes. Potentially able to adjust the font. These are the things I need added it to include.
Head shot (attached)
Text Box for Name
Text Box for phone number
Text box for email
KTW Logo (attached)
Maybe a blue banner at the top or some background boxes that are blue or grey. Here are the pantone colors that our company uses.

CORE COLOR
100c 91m 17y 6k 38r 58g 128b Hex #263A80 Pantone 7687 C

CORE CONTRAST COLOR
36c 29m 28y 0k 168r 168g 170b Hex #669999 Pantone Cool Gray 6C

I also attached some examples of what we have been looking at. Instead of green add the blue...instead of black maybe just be white.

Thank you

```html
<!DOCTYPE html>
<html lang="en">
<head>
<meta charset="utf-8">
<title>Professional Bio Template</title>
<link rel="stylesheet" href="https://fonts.googleapis.com/css2?family=Bebas+Neue&family=Arimo:wght@400;700&display=swap">
<style>
  :root {
    --core-blue: #263A80;
    --contrast-gray: #A8A8AA;
    --backdrop: #C0C0C0;
    --page: #FFFFFF;
    --ink: #333333;
  }
  * { box-sizing: border-box; margin: 0; padding: 0; }
  html, body { width: 1200px; height: 1200px; overflow: hidden; }
  body { background: var(--backdrop); font-family: "Arimo", Arial, sans-serif; position: relative; }

  .bio-page {
    position: absolute; left: 197px; top: 30px;
    width: 806px; height: 1140px;
    background: var(--page);
    overflow: hidden;
  }
  .top-band { position: absolute; left: 0; top: 0; width: 100%; height: 79px; background: var(--core-blue); }

  .header-panel {
    position: absolute; left: 0; top: 99px; width: 100%; height: 157px;
    background: linear-gradient(90deg, #C9C9CB 0%, #E4E4E6 35%, #F3F3F4 70%, #FFFFFF 100%);
  }
  .header-rule { position: absolute; left: 0; top: 96px; width: 100%; height: 3px; background: #FFFFFF; }

  .building-backdrop {
    position: absolute; left: 0; top: 700px; width: 100%; height: 384px;
    background: linear-gradient(180deg, rgba(236,236,240,0) 0%, #EFEFF2 45%, #E6E6EA 100%);
  }

  .photo-shadow {
    position: absolute; left: 59px; top: 145px; width: 168px; height: 231px;
    background: linear-gradient(90deg, #A9A9AB 0%, #D6D6D8 60%, #F0F0F0 100%);
  }
  .headshot {
    position: absolute; left: 73px; top: 132px; width: 154px; height: 231px;
    background: radial-gradient(ellipse at 50% 35%, #5A5A5C 0%, #3A3A3C 55%, #2B2B2D 100%);
  }

  .name {
    position: absolute; left: 267px; top: 144px;
    font-family: "Bebas Neue", Impact, sans-serif; font-size: 42px; font-weight: 400;
    color: var(--core-blue); letter-spacing: 0.2px; white-space: nowrap;
  }
  .name .gap { display: inline-block; width: 10px; }

  .contact-divider { position: absolute; top: 193px; width: 1px; height: 81px; background: #C4C4C6; }
  .contact {
    position: absolute; top: 207px; display: flex; align-items: center; gap: 12px;
    font-size: 14.5px; font-weight: 700; color: var(--ink); white-space: nowrap;
  }
  .contact svg { width: 16px; height: 16px; fill: var(--core-blue); }

  .bio-section { position: absolute; left: 267px; width: 457px; color: var(--ink); }
  .bio-section h2 { font-size: 19px; font-weight: 700; line-height: 22px; margin-bottom: 1px; }
  .bio-section p { font-size: 13.4px; line-height: 19px; }

  .logo-panel {
    position: absolute; left: 59px; top: 923px; width: 168px; height: 161px;
    background: #FFFFFF; display: flex; align-items: center; justify-content: center; gap: 8px;
  }
  .logo-mark { width: 14px; height: 14px; background: var(--core-blue); }
  .logo-name {
    font-family: "Arimo", Arial, sans-serif; font-weight: 700; font-size: 30px;
    color: var(--core-blue); letter-spacing: 1px;
  }

  .footer-rule { position: absolute; left: 0; top: 1084px; width: 100%; height: 10px;
    background: linear-gradient(180deg, #E8E8EA 0%, #FFFFFF 45%, #CFCFD1 100%); }
  .footer-band { position: absolute; left: 0; top: 1106px; width: 100%; height: 34px; background: var(--core-blue); }
</style>
</head>
<body>
  <main class="bio-page">
    <div class="top-band"></div>

    <div class="header-panel"></div>
    <div class="header-rule"></div>
    <div class="building-backdrop" role="img" aria-label="Faint photograph of modern office building facades"></div>

    <div class="photo-shadow"></div>
    <div class="headshot" role="img" aria-label="Headshot photo of the professional in a dark blazer"></div>

    <h1 class="name">First Name<span class="gap"></span> Last Name</h1>

    <div class="contact-divider" style="left:267px"></div>
    <div class="contact-divider" style="left:456px"></div>
    <div class="contact-divider" style="left:727px"></div>

    <div class="contact" style="left:294px">
      <svg viewBox="0 0 24 24" aria-hidden="true"><path d="M6.6 10.8c1.4 2.8 3.8 5.1 6.6 6.6l2.2-2.2c.3-.3.7-.4 1-.2 1.1.4 2.3.6 3.6.6.6 0 1 .4 1 1V20c0 .6-.4 1-1 1C10.6 21 3 13.4 3 4c0-.6.4-1 1-1h3.5c.6 0 1 .4 1 1 0 1.3.2 2.5.6 3.6.1.3 0 .7-.2 1l-2.3 2.2z"/></svg>
      <span>+000 000 00 00</span>
    </div>
    <div class="contact" style="left:484px">
      <svg viewBox="0 0 24 24" aria-hidden="true"><path d="M2 5h20v2l-10 6L2 7z"/><path d="M2 9l10 6 10-6v10H2z"/></svg>
      <span>info@companyname.com</span>
    </div>

    <section class="bio-section" style="top:290px">
      <h2>Lorem ipsum dolor sit amet,</h2>
      <p>consectetuer adipiscing elit, sed diam nonummy nibh euismod tincidunt ut laoreet dolore magna aliquam erat volutpat. Ut wisi enim ad minim veniam, quis nostrud exerci tation ullamcorper suscipit lobortis nisl ut aliquip ex ea commodo consequat. Duis autem vel eum iriure dolor in hendrerit in vulpu-<br>tate velit esse molestie consequat, vel illum dolore eu feugiat nulla facilisis at vero eros et accumsan et iusto odio dignissim qui blandit praesent luptatum zzril delenit augue duis dolore te feugait nulla facilisi.</p>
    </section>

    <section class="bio-section" style="top:466px">
      <h2>Lorem ipsum dolor sit amet,</h2>
      <p>cons ectetuer adipiscing elit, sed diam nonummy nibh euismod tincidunt ut laoreet dolore magna aliquam erat volutpat. Ut wisi enim ad minim veniam, quis nostrud exerci tation ullamcorper suscipit lobortis nisl ut aliquip ex ea commodo consequat.</p>
    </section>

    <section class="bio-section" style="top:585px">
      <h2>Lorem ipsum dolor sit amet,</h2>
      <p>consectetuer adipiscing elit, sed diam nonummy nibh euismod tincidunt ut laoreet dolore magna aliquam erat volutpat. Ut wisi enim ad minim veniam, quis nostrud exerci tation ullamcorper suscipit lobortis nisl ut aliquip ex ea commodo consequat. Duis autem vel eum iriure dolor in hendrerit in vulpu-<br>tate velit esse molestie consequat, vel illum dolore eu feugiat nulla facilisis at vero eros et accumsan et iusto odio dignissim qui blandit praesent luptatum zzril delenit augue duis dolore te feugait nulla facilisi.</p>
    </section>

    <section class="bio-section" style="top:761px">
      <h2>Lorem ipsum dolor sit amet,</h2>
      <p>cons ectetuer adipiscing elit, sed diam nonummy nibh euismod tincidunt ut laoreet dolore magna aliquam erat volutpat. Ut wisi enim ad minim veniam, quis nostrud exerci tation ullamcorper suscipit lobortis nisl ut aliquip ex ea commodo consequat.<br>Lorem ipsum dolor sit amet, consectetuer adipiscing elit, sed diam nonummy<br>nibh euismod tincidunt ut laoreet dolore magna aliquam erat volutpat. Ut wisi<br>enim ad minim veniam, quis nostrud exerci tation ullamcorper suscipit<br>lobortis nisl ut aliquip ex ea commodo</p>
    </section>

    <section class="bio-section" style="top:953px">
      <h2>Lorem ipsum dolor sit amet,</h2>
      <p>cons ectetuer adipiscing elit, sed diam nonummy nibh euismod tincidunt ut laoreet dolore magna aliquam erat volutpat. Ut wisi enim ad minim veniam, quis nostrud exerci tation ullamcorper suscipit lobortis nisl ut aliquip ex ea commodo consequat.</p>
    </section>

    <div class="logo-panel">
      <span class="logo-mark"></span>
      <span class="logo-name">KTW</span>
    </div>

    <div class="footer-rule"></div>
    <div class="footer-band"></div>
  </main>
</body>
</html>
```